Create Bramble Learning Studio a card design that will stick in the mind of prospects.

Bramble Learning Studio specialises designs and produces training video, animation, illustration and text.

We need a card design that oozes class and leaves the prospect brimming with confidence.

The design will feature the Bramble Learning Studio all black logo (uploaded). The design may also use the shade of orange from the orange version of the logo (uploaded). Note, just the color is to be used e.g. for the back of the card, not the orange logo itself.

The Bramble brand is about authenticity, quality, maturity and assurance. We are a safe buy when it comes to the prospects next project.

Target Market(s)

The primary target is training managers or others who are responsible for choosing to hire companies to produce their training media e.g. video. This will usually be a large spend so they need to have confidence.

Industry/Entity Type

Training

Contact Information for Business Card

FRONT:

Bramble Learning Studio
Phone: 03 5126 4390
1st Floor, 417 Fenwick Street
Glen Orrin
VIC 3271
Australia
www.bramblelearn.com.au

Colin Ashby
Founder and Lead Consultant
mobile: +61 3 0462 905 318
email: colin@bramblelearn.com.au

BACK:
Specialising in design and production of training:

video
animation
illustration
text

for delivery via internet, intranet and/or LMS.

Number of Pages Required

4 page

Font styles to use
Sans Serif

Requirements
Must have
• The black logo uploaded with the brief.
Nice to have
• The inclusion of the shade of orange found in the orange logo also uploaded with the brief. One example would be having the back of the card in this orange and using a white font for the text. But I want the designer to work this out.
Should not have
• No colours other than black and the orange included in the uploaded orange logo.

```html
<!DOCTYPE html>
<html lang="en">
<head>
<meta charset="utf-8">
<title>Bramble Learning Studio — Business Card</title>
<link href="https://fonts.googleapis.com/css2?family=Montserrat:wght@400;500;600;700&display=swap" rel="stylesheet">
<style>
  :root {
    --orange: #f15a22;
    --black: #0b0b0b;
    --white: #ffffff;
    --ink: #1a1a1a;
    --stage: #3a3a3a;
  }
  * { margin: 0; padding: 0; box-sizing: border-box; }
  html, body { width: 1200px; height: 900px; overflow: hidden; }
  body {
    background: var(--stage);
    font-family: "Montserrat", Arial, sans-serif;
    position: relative;
  }
  .card {
    position: absolute;
    width: 560px;
    height: 320px;
    border-radius: 22px;
    overflow: hidden;
  }
  /* Card back: black with brand name and services */
  .card--back {
    left: 60px; top: 90px;
    background: var(--black);
    color: var(--white);
    text-align: center;
  }
  .brand {
    display: flex;
    align-items: center;
    justify-content: center;
    gap: 12px;
    white-space: nowrap;
  }
  .brand__dot {
    width: 20px; height: 20px; border-radius: 50%;
    flex: none;
  }
  .brand__name {
    font-weight: 700;
    letter-spacing: 0.5px;
  }
  .card--back .brand { margin-top: 86px; }
  .card--back .brand__dot { background: var(--orange); }
  .card--back .brand__name { color: var(--orange); font-size: 56px; }
  .services {
    margin-top: 48px;
    font-size: 20px;
    font-weight: 500;
    letter-spacing: 0.3px;
  }
  .services .sep { color: var(--orange); }
  .website { margin-top: 6px; font-size: 18px; font-weight: 500; }
  .accent { color: var(--orange); }

  /* Card front: white with contact details */
  .card--front {
    left: 580px; top: 490px;
    background: var(--white);
    color: var(--ink);
  }
  .card__arcs { position: absolute; inset: 0; }
  .contact {
    position: absolute;
    left: 34px; top: 122px;
    font-size: 13px;
    line-height: 1.3;
  }
  .contact__name {
    color: var(--orange);
    font-size: 25px;
    font-weight: 700;
    line-height: 1.1;
  }
  .contact__title { font-size: 14px; font-weight: 500; margin-bottom: 6px; }
  .contact__address { margin-bottom: 8px; }
  .contact__list { list-style: none; }
  .contact__list li { display: flex; align-items: center; gap: 8px; }
  .contact__list svg { width: 12px; height: 12px; flex: none; }
  .card--front .brand {
    position: absolute;
    right: 26px; top: 118px;
  }
  .card--front .brand__dot { background: var(--black); width: 18px; height: 18px; }
  .card--front .brand__name { color: var(--black); font-size: 32px; }
</style>
</head>
<body>

<section class="card card--back" aria-label="Card back">
  <div class="brand">
    <span class="brand__dot"></span>
    <span class="brand__name">Bramble</span>
  </div>
  <p class="services">Video <span class="sep">-</span> Animation <span class="sep">-</span> Illustration <span class="sep">-</span> Text</p>
  <p class="website">www.<span class="accent">bramblelearn</span>.com.au</p>
</section>

<section class="card card--front" aria-label="Card front">
  <svg class="card__arcs" viewBox="0 0 560 320" aria-hidden="true">
    <path d="M150 0 C 300 20, 380 170, 300 320" fill="none" stroke="#0b0b0b" stroke-width="7"/>
    <path d="M138 6 C 285 26, 362 172, 284 320" fill="none" stroke="#f15a22" stroke-width="7"/>
  </svg>

  <div class="contact">
    <h1 class="contact__name">Colin Ashby</h1>
    <p class="contact__title">Founder and Lead Consultant</p>
    <p class="contact__address">1st Floor, 417 Fenwick Street<br>Glen Orrin<br>VIC 3271</p>
    <ul class="contact__list">
      <li>
        <svg viewBox="0 0 24 24"><path fill="#f15a22" d="M6.6 10.8a15 15 0 0 0 6.6 6.6l2.2-2.2a1 1 0 0 1 1-.25 11.4 11.4 0 0 0 3.6.57 1 1 0 0 1 1 1V20a1 1 0 0 1-1 1A17 17 0 0 1 3 4a1 1 0 0 1 1-1h3.5a1 1 0 0 1 1 1 11.4 11.4 0 0 0 .57 3.6 1 1 0 0 1-.25 1z"/></svg>
        <span>03 5126 4390</span>
      </li>
      <li>
        <svg viewBox="0 0 24 24"><rect x="6" y="2" width="12" height="20" rx="2" fill="none" stroke="#f15a22" stroke-width="2.4"/><circle cx="12" cy="18" r="1.3" fill="#f15a22"/></svg>
        <span>+61 3 0462 905 318</span>
      </li>
      <li>
        <svg viewBox="0 0 24 24"><rect x="2" y="5" width="20" height="14" rx="1.5" fill="none" stroke="#f15a22" stroke-width="2.4"/><path d="M3 6l9 7 9-7" fill="none" stroke="#f15a22" stroke-width="2.4"/></svg>
        <span>colin@bramblelearn.com.au</span>
      </li>
      <li>
        <svg viewBox="0 0 24 24"><circle cx="12" cy="12" r="10" fill="none" stroke="#f15a22" stroke-width="2.2"/><path d="M2 12h20M12 2c3 3 3 17 0 20M12 2c-3 3-3 17 0 20" fill="none" stroke="#f15a22" stroke-width="2"/></svg>
        <span>www.<span class="accent">bramblelearn</span>.com.au</span>
      </li>
    </ul>
  </div>

  <div class="brand">
    <span class="brand__dot"></span>
    <span class="brand__name">Bramble</span>
  </div>
</section>

</body>
</html>
```